KORBALT

The business want a professional looking business card. We have a scetch we will add but want the extra upgrade, and would like more suggestions for variations of our business cards.

```html
<!DOCTYPE html>
<html lang="en">
<head>
<meta charset="UTF-8">
<title>KORBALT – Business Card</title>
<link rel="stylesheet" href="https://fonts.googleapis.com/css2?family=Montserrat:wght@400;500&display=swap">
<style>
  :root {
    --page-bg: #eef1f3;
    --card-cream: #fcf4e6;
    --ink-gold: #8a6326;
    --gold-light: #e2c48a;
    --gold-mid: #b8893a;
    --gold-deep: #8a6326;
  }
  * { box-sizing: border-box; margin: 0; padding: 0; }
  html, body {
    width: 1103px; height: 1200px; overflow: hidden;
    background: var(--page-bg);
    font-family: "Montserrat", Arial, sans-serif;
    color: var(--ink-gold);
  }
  .sheet {
    position: relative; width: 1103px; height: 1200px;
    display: flex; flex-direction: column; align-items: center;
    justify-content: center; gap: 60px;
  }
  .card {
    position: relative; width: 960px; height: 530px;
    background: var(--card-cream);
    overflow: hidden;
    box-shadow: 18px 22px 34px rgba(60, 64, 70, 0.28);
  }

  /* Front */
  .brand {
    position: absolute; left: 0; width: 960px; top: 150px;
    display: flex; flex-direction: column; align-items: center;
  }
  .brand-row { display: flex; align-items: center; gap: 26px; }
  .brand-name {
    font-weight: 500; font-size: 70px; letter-spacing: 10px;
    color: var(--ink-gold); line-height: 1;
  }
  .brand-dot {
    width: 46px; height: 46px; border-radius: 50%;
    background: var(--gold-mid);
  }
  .brand-since {
    margin-top: 18px; margin-right: 72px;
    font-weight: 500; font-size: 18px; letter-spacing: 7px;
    color: var(--ink-gold);
  }
  .front-ornament {
    position: absolute; left: 277px; top: 336px;
    width: 400px; height: 194px;
    background: radial-gradient(ellipse at 50% 100%, var(--gold-mid) 0%, var(--gold-light) 45%, rgba(252,244,230,0) 75%);
  }

  /* Back */
  .holder { position: absolute; left: 53px; top: 60px; }
  .holder-company {
    font-weight: 500; font-size: 46px; letter-spacing: 1px; line-height: 1.1;
  }
  .holder-role { margin-top: 24px; font-weight: 500; font-size: 47px; line-height: 1.05; }
  .holder-name { margin-top: 4px; font-weight: 400; font-size: 32px; letter-spacing: 0.5px; }

  .contacts {
    position: absolute; left: 53px; top: 350px;
    list-style: none; display: flex; flex-direction: column; gap: 12px;
  }
  .contact { display: flex; align-items: center; gap: 18px; font-size: 32px; line-height: 30px; }
  .contact-icon { width: 26px; height: 26px; flex: none; }

  .back-ornament {
    position: absolute; right: 0; top: 100px;
    width: 170px; height: 330px;
    background: radial-gradient(ellipse at 100% 50%, var(--gold-mid) 0%, var(--gold-light) 48%, rgba(252,244,230,0) 78%);
  }
</style>
</head>
<body>
<main class="sheet">

  <section class="card card-front" aria-label="Business card front">
    <div class="brand">
      <div class="brand-row">
        <span class="brand-name">KORBALT</span>
        <span class="brand-dot"></span>
      </div>
      <span class="brand-since">SINCE 2026</span>
    </div>
    <div class="front-ornament" role="img" aria-label="Gold foil brand ornament rising from the bottom edge"></div>
  </section>

  <section class="card card-back" aria-label="Business card back">
    <div class="holder">
      <p class="holder-company">KORBALT H DALSRUD</p>
      <p class="holder-role">CEO &amp; Founder</p>
      <p class="holder-name">Lars Henrik Dalsrud</p>
    </div>

    <ul class="contacts">
      <li class="contact">
        <svg class="contact-icon" viewBox="0 0 26 26" aria-hidden="true">
          <circle cx="13" cy="13" r="11.5" fill="none" stroke="var(--ink-gold)" stroke-width="1.5"/>
          <rect x="9.5" y="6.5" width="7" height="13" rx="1.5" fill="none" stroke="var(--ink-gold)" stroke-width="1.5"/>
          <circle cx="13" cy="17" r="0.9" fill="var(--ink-gold)"/>
        </svg>
        <span>004791234567</span>
      </li>
      <li class="contact">
        <svg class="contact-icon" viewBox="0 0 26 26" aria-hidden="true">
          <circle cx="13" cy="13" r="11.5" fill="none" stroke="var(--ink-gold)" stroke-width="1.5"/>
          <rect x="7" y="9" width="12" height="8.5" rx="1" fill="var(--ink-gold)"/>
          <path d="M7.5 9.5 L13 14 L18.5 9.5" fill="none" stroke="var(--card-cream)" stroke-width="1.2"/>
        </svg>
        <span>korbalt.llc@mailhub.com</span>
      </li>
      <li class="contact">
        <svg class="contact-icon" viewBox="0 0 26 26" aria-hidden="true">
          <circle cx="13" cy="13" r="11.5" fill="none" stroke="var(--ink-gold)" stroke-width="1.5"/>
          <circle cx="13" cy="13" r="6.5" fill="none" stroke="var(--ink-gold)" stroke-width="1.2"/>
          <ellipse cx="13" cy="13" rx="2.8" ry="6.5" fill="none" stroke="var(--ink-gold)" stroke-width="1.1"/>
          <line x1="6.5" y1="13" x2="19.5" y2="13" stroke="var(--ink-gold)" stroke-width="1.1"/>
        </svg>
        <span>www.korbalt.llc</span>
      </li>
    </ul>

    <div class="back-ornament" role="img" aria-label="Gold foil brand ornament cropped at the right edge"></div>
  </section>

</main>
</body>
</html>
```